RW Hollis LLC Business Card - Civil Engineering & Consulting Firm

We need a Business Card that is elegant, and masculine.  It is our Professional Civil Engineering & Consulting Company located in San Antonio TX (Not s construction or builder firm- no gears & no tool images please). We provide civil engineering services including  commercial site plans, grading and drainage plans, utility plans, hydraulics and hydrology, land planning, utility coordination, and other general civil engineering services related to commercial and residential development.
We have 2 existing Logos. We would like to convey reliability, strength, trustworthiness and attention to detail.  Blues and orange tones as per logo We are OK with the use of a darker blue in the mix.  We have 2 logo versions - Full Company Name Logo to go on the back of card, & Small Icon Logo for the front w/ personal Info.

Target Market(s)
Architects, Real Estate Developers, Other Strctural Engineers, Surveyers, General Contractors
Industry/Entity Type
Professional Civil Engineering
Contact Information for Business Card
Name, Position, Address, Cell & Office #, email, and company website
Font styles to use
Other font styles liked:
- Avian
Requirements
Should not have
- No Tools, No Gears, no Cranes, or Construction Equipment.

```html
<!DOCTYPE html>
<html lang="en">
<head>
<meta charset="utf-8">
<title>RW Hollis LLC – Business Card</title>
<link rel="stylesheet" href="https://fonts.googleapis.com/css2?family=Montserrat:wght@400;500;700&display=swap">
<style>
  :root{
    --stage:#3b3b3b;
    --card:#1c1c1d;
    --card-edge:#7fb0df;
    --blue:#7fb0df;
    --orange:#f0962c;
    --text:#ededed;
    --pattern-a:#141415;
    --pattern-b:#2b2b2d;
  }
  *{box-sizing:border-box;margin:0;padding:0}
  html,body{width:1200px;height:801px;overflow:hidden;background:var(--stage);
    font-family:"Montserrat",Arial,sans-serif}
  .stage{position:relative;width:1200px;height:801px;display:flex;
    align-items:center;justify-content:center;gap:40px}
  .card{width:540px;height:309px;background:var(--card);position:relative;
    border-bottom:2px solid var(--card-edge);border-left:2px solid var(--card-edge)}
  .card-front{display:flex;align-items:center}
  .brand{width:272px;padding-left:34px;display:flex;flex-direction:column;gap:10px}
  .brand-name{display:flex;align-items:center;gap:10px;color:var(--blue);
    font-weight:500;font-size:26px;letter-spacing:2px}
  .brand-square{width:14px;height:14px;background:var(--orange);flex:none}
  .brand-tagline{color:var(--orange);font-size:9px;letter-spacing:4px;padding-left:24px}
  .divider{width:1px;height:150px;background:var(--blue);opacity:.7}
  .contact{padding-left:24px;color:var(--text);font-size:12px;line-height:1.45}
  .contact-name{color:var(--blue);font-weight:700;font-size:17px;letter-spacing:.5px}
  .contact-role{margin-bottom:10px}
  .contact-address{margin-bottom:10px}
  .contact-line{display:flex;align-items:center;gap:8px}
  .contact-line svg{width:10px;height:10px;flex:none;fill:var(--orange)}
  .card-back{overflow:hidden}
  .back-pattern{position:absolute;inset:0;
    background:linear-gradient(120deg,var(--pattern-a) 0%,var(--pattern-b) 70%,#303033 100%)}
  .back-brand{position:absolute;left:50%;top:50%;transform:translate(-50%,-50%);
    display:flex;align-items:center;gap:8px;color:var(--blue);font-weight:500;
    font-size:16px;letter-spacing:2px}
  .back-brand .brand-square{width:10px;height:10px}
</style>
</head>
<body>
<main class="stage">
  <section class="card card-front">
    <div class="brand">
      <div class="brand-name"><span class="brand-square"></span>RW HOLLIS LLC</div>
      <div class="brand-tagline">CONSULTING ENGINEERS</div>
    </div>
    <div class="divider"></div>
    <div class="contact">
      <div class="contact-name">DANIEL VARGA</div>
      <div class="contact-role">President</div>
      <div class="contact-address">1840 Harbor View Drive<br>Seal Cove CA 92600</div>
      <div class="contact-line">
        <svg viewBox="0 0 10 10"><rect x="2" y="0" width="6" height="10" rx="1"/></svg>555-310-4827</div>
      <div class="contact-line">
        <svg viewBox="0 0 10 10"><path d="M2 0l2 3-1 1.2c.6 1.3 1.5 2.2 2.8 2.8L7 6l3 2-1 2C4 10 0 6 0 1z"/></svg>555-310-4828</div>
      <div class="contact-line">
        <svg viewBox="0 0 10 10"><path d="M0 2h10v6H0zM0 2l5 3.5L10 2" /></svg>info@rwhollisconsulting.com</div>
      <div class="contact-line">
        <svg viewBox="0 0 10 10"><circle cx="5" cy="5" r="5"/></svg>www.rwhollisconsulting.com</div>
    </div>
  </section>
  <section class="card card-back">
    <div class="back-pattern" role="img" aria-label="Tone-on-tone repeating brand pattern across the card back"></div>
    <div class="back-brand"><span class="brand-square"></span>RW HOLLIS LLC</div>
  </section>
</main>
</body>
</html>
```